Webdesign für Immobilienmanagement
Zielgruppe
Immobilienmanagement Unternehmen / allg. Hausverwaltung , Hausmeisterservice, Grünanlagenpflege, Unterhaltsreinigung, Winterdienst
Zielgruppe: Mieter und Wohnungseigentümer
Aufgabenstellung
Farben: weiß/grün
keine Kopie der alten Seite
nutzerfreundliche Unternehmenswebseite
Logo vorhanden auf alter Webseite

```html
<!DOCTYPE html>
<html lang="de">
<head>
<meta charset="utf-8">
<title>Lindenau Immobilien-Management</title>
<link href="https://fonts.googleapis.com/css2?family=Roboto:wght@400;500;700&display=swap" rel="stylesheet">
<style>
:root{
  --green:#4aaa2f;
  --text:#333;
  --muted:#888;
  --line:#c8c8c8;
  --white:#fff;
}
*{box-sizing:border-box;margin:0;padding:0}
html,body{width:1200px;height:2726px;overflow:hidden;background:var(--white)}
body{font-family:'Roboto',sans-serif;color:var(--text);position:relative}
.abs{position:absolute}
.topbar{left:88px;top:10px;font-size:10px;display:flex;gap:16px;align-items:center}
.topbar span{display:flex;align-items:center;gap:4px}
.mainnav{left:88px;top:49px;display:flex;gap:52px;font-size:13px;font-weight:500}
.mainnav .active{border-bottom:3px solid var(--green);padding-bottom:3px}
.brand{display:flex;align-items:center;gap:10px;font-weight:700;color:var(--green);font-size:24px}
.brand i{display:block;width:22px;height:22px;background:var(--green)}
.header-brand{right:90px;top:28px}
.header-rule{left:0;top:83px;width:1200px;height:1px;background:#e6e6e6}
.hero{left:0;top:84px;width:1200px;height:404px;background:linear-gradient(180deg,#c9cfd3 0%,#dfe3e4 35%,#8e9a6a 48%,#7d7462 62%,#5f6a45 100%)}
.hero-box{left:0;top:329px;width:508px;height:124px;background:var(--green);border-radius:0 10px 10px 0;color:var(--white);padding:26px 0 0 88px}
.hero-box h1{font-size:32px;font-weight:700}
.hero-box p{font-size:15px;font-weight:500;margin-top:10px}
.section-title{left:260px;font-size:26px;font-weight:500}
.underline{left:260px;width:92px;height:5px;background:var(--green)}
.btn{display:inline-flex;align-items:center;justify-content:center;background:var(--green);color:var(--white);font-size:12.5px;font-weight:700;border-radius:15px;height:30px;padding:0 16px}
.news-card{left:260px;top:622px;width:680px;height:217px;box-shadow:0 2px 8px rgba(0,0,0,.18);display:flex;background:var(--white)}
.news-img{width:196px;height:217px;background:linear-gradient(135deg,#4a3a2a,#6b7e3a 60%,#2f6b4a)}
.news-body{padding:19px 24px;font-size:14px}
.news-meta{display:flex;align-items:baseline;gap:16px}
.green-h{color:var(--green);font-weight:700;font-size:17px}
.news-body h3{margin-top:12px}
.news-body h4{font-size:14.5px;font-weight:500;margin-top:10px}
.news-body p{margin-top:10px;line-height:19px}
.news-body .btn{margin-top:16px}
.topic-img{width:306px;height:306px}
.topic-text{width:310px;font-size:14px}
.topic-text p{margin-top:12px;line-height:19px}
.ticks{list-style:none;margin-top:24px;font-weight:500;font-size:14px}
.ticks li{line-height:19px;padding-left:20px;position:relative}
.ticks li::before{content:"";position:absolute;left:4px;top:6px;width:8px;height:8px;background:var(--green)}
.topic-text .btn{margin-top:18px}
.intro{left:260px;top:2203px;width:430px;font-size:14px;line-height:19px}
.field{height:34px;border:1px solid var(--line);color:#999;font-size:14px;padding:8px 16px}
.consent{left:260px;top:2497px;width:388px;font-size:8px;line-height:11.5px;color:#555;padding-left:17px}
.consent::before{content:"";position:absolute;left:0;top:1px;width:11px;height:11px;background:#333}
.consent em{color:var(--green);font-style:normal}
.address{left:691px;font-size:14px;line-height:19px}
.footer-rule{left:0;top:2638px;width:1200px;height:4px;background:#e0e0e0}
.footer-links{left:90px;top:2675px;font-size:8.5px;color:#444}
.footer-brand{right:100px;top:2665px}
</style>
</head>
<body>

<header>
  <div class="abs topbar">
    <span><svg width="9" height="9" viewBox="0 0 10 10"><path d="M2 0l2 2-1 2a6 6 0 0 0 3 3l2-1 2 2-1 2C4 10 0 6 0 2z" fill="#333"/></svg>Beratung</span>
    <span><svg width="10" height="8" viewBox="0 0 10 8"><rect width="10" height="8" fill="#333"/><path d="M0 0l5 4 5-4" stroke="#fff" fill="none"/></svg>Kontakt</span>
    <span><svg width="9" height="9" viewBox="0 0 10 10"><path d="M4 0h2v5h2L5 8 2 5h2zM0 9h10v1H0z" fill="#333"/></svg>Downloads</span>
  </div>
  <nav class="abs mainnav">
    <span class="active">Home</span><span>Über Uns</span><span>Hausverwaltung</span><span>Hausmeister</span>
  </nav>
  <div class="abs brand header-brand">Lindenau <i></i></div>
  <div class="abs header-rule"></div>
</header>

<section>
  <div class="abs hero" role="img" aria-label="Luftaufnahme einer Kleinstadt mit Dächern, Feldern und Sportplatz"></div>
  <div class="abs hero-box">
    <h1>Herzlich Willkommen</h1>
    <p>Ihr zuverlässiger Dienstleister rund um die Immobilien</p>
  </div>
</section>

<section>
  <h2 class="abs section-title" style="top:534px">Aktuelles</h2>
  <div class="abs underline" style="top:584px"></div>
  <article class="abs news-card">
    <div class="news-img" role="img" aria-label="Gärtner beim Einpflanzen in Erde"></div>
    <div class="news-body">
      <div class="news-meta"><span class="green-h">Neuer Artikel!</span><span>Montag, 01. Januar 2024</span></div>
      <h3 class="green-h">Wohnen und arbeiten im Grünen</h3>
      <h4>Zuverlässige Verwaltung und günstige Konditionen</h4>
      <p>Schauen Sie sich unser Leistungsangebot an und überzeugen Sie sich selbst von den Vorteilen, die wir Ihnen bieten können.</p>
      <span class="btn">Weiterlesen</span>
    </div>
  </article>
  <span class="abs btn" style="left:260px;top:882px">Zu allen Meldungen</span>
</section>

<section>
  <h2 class="abs section-title" style="top:958px">Unsere Beratungsthemen</h2>
  <div class="abs underline" style="top:1010px"></div>

  <div class="abs topic-img" style="left:260px;top:1046px;background:linear-gradient(160deg,#f4f4f4,#e6ece2 50%,#7fb85a 85%,#9ba59a)" role="img" aria-label="Modernes weißes Wohnhaus mit grünen Balkonen"></div>
  <div class="abs topic-text" style="left:634px;top:1091px">
    <h3 class="green-h">Beratung zur Hausverwaltung</h3>
    <p>Sie haben Fragen zu unseren Leistungen Verwaltung und Betreuung? Wir beraten Sie gern unter anderem zu folgenden Themen:</p>
    <ul class="ticks"><li>Allgemeine Verwaltung</li><li>Kaufmännische Betreuung</li><li>Technische Betreuung</li></ul>
    <span class="btn">Mehr erfahren</span>
  </div>

  <div class="abs topic-text" style="left:260px;top:1431px">
    <h3 class="green-h">Beratung zum Hausmeisterservice</h3>
    <p>Sie haben Fragen rund um unser Angebot zum Hausmeisterservice? Wir beraten Sie gern unter anderem zu folgenden Themen:</p>
    <ul class="ticks"><li>Hausmeisterservice</li><li>Grünanlagenpflege</li><li>Winterdienst</li><li>Unterhaltsreinigung</li></ul>
    <span class="btn">Mehr erfahren</span>
  </div>
  <div class="abs topic-img" style="left:634px;top:1395px;background:linear-gradient(135deg,#b7c0cc,#eef0f2 45%,#d7dbe0 70%,#4a5d80)" role="img" aria-label="Handwerker lehnt an einem weißen Transporter"></div>

  <div class="abs topic-img" style="left:260px;top:1756px;background:linear-gradient(135deg,#d9dde2,#f1ece8 40%,#e8d6d8 65%,#8a8f96)" role="img" aria-label="Mitarbeiterin am Schreibtisch im Büro"></div>
  <div class="abs topic-text" style="left:634px;top:1810px">
    <h3 class="green-h">Beratung zum Thema Notdienst</h3>
    <p>Sie haben in Notfällen nur einen Ansprechpartner und wir koordinieren für Sie die entsprechenden Arbeiten.</p>
    <ul class="ticks"><li>Schnell &amp; kompetent</li><li>24 Stunden am Tag, 7 Tage die Woche</li></ul>
    <span class="btn">Mehr erfahren</span>
  </div>
</section>

<section>
  <h2 class="abs section-title" style="top:2107px">Kontakt &amp; Rückrufservice</h2>
  <div class="abs underline" style="top:2157px"></div>
  <p class="abs intro">Sie haben eine Frage zu unserem Serviceangebot? Dann füllen Sie einfach folgendes Formular aus und wir melden uns schnellst­möglich bei Ihnen.</p>

  <h3 class="abs green-h" style="left:260px;top:2277px">Schreiben Sie uns</h3>
  <div class="abs field" style="left:260px;top:2318px;width:186px">Vorname</div>
  <div class="abs field" style="left:461px;top:2318px;width:187px">Name</div>
  <div class="abs field" style="left:260px;top:2362px;width:186px">E-Mailadresse</div>
  <div class="abs field" style="left:461px;top:2362px;width:187px">Telefon</div>
  <div class="abs field" style="left:260px;top:2407px;width:388px">Betreff</div>
  <div class="abs field" style="left:260px;top:2451px;width:388px">Nachricht</div>
  <p class="abs consent">Ich stimme zu, dass meine Angaben aus dem Kontaktformular zur Beantwortung meiner Anfrage erhoben und verarbeitet werden. Die Daten werden nach abgeschlossener Bearbeitung Ihrer Anfrage gelöscht. Hinweis: Sie können Ihre Einwilligung jederzeit für die Zukunft per E-Mail an <em>info@lindenau-immobilien.de</em> widerrufen. Detaillierte Informationen zum Umgang mit Nutzerdaten finden Sie in unserer <em>Datenschutzerklärung</em>.</p>
  <span class="abs btn" style="left:260px;top:2567px;width:113px">Senden</span>

  <h3 class="abs green-h" style="left:691px;top:2277px">Anschrift</h3>
  <p class="abs address" style="top:2310px">Lindenau Immobilien-Management GmbH<br>Birkenweg 8 a<br>04600 Talstadt</p>
  <h3 class="abs green-h" style="left:691px;top:2391px">Kontaktdaten</h3>
  <p class="abs address" style="top:2424px">Tel.: +49 30 1234 567 0<br>Fax: +49 30 1234 567 45<br>info@lindenau-immobilien.de</p>
</section>

<footer>
  <div class="abs footer-rule"></div>
  <p class="abs footer-links">Impressum | Datenschutz | Kontakt | Downloads &nbsp;| Partnerlinks</p>
  <div class="abs brand footer-brand">Lindenau <i></i></div>
</footer>

</body>
</html>
```